Business Card Design for Cybersecurity Company - Quorvent Systems

We need a business card design for our new cybersecurity company, Quorvent. We’re going for a clean, hi tech look that feels modern, premium, and trustworthy. We want a design that really stands out and makes people say WOW when we hand it over!

Quorvent delivers reliable IT support and managed services for small and mid sized businesses. We help companies stay secure, efficient, and connected through proactive monitoring, cybersecurity services, cloud management, and remote support.

Target Market(s)

Designers should target small and mid sized businesses that need dependable cybersecurity and IT support.

Industry/Entity Type

Cybersecurity, Managed Service Provider, IT services

Contact Information for Business Card

Contact information

Requirements
Must have
• The card should look clean, modern, and tech focused, with the Quorvent logo, clear contact info, and strong readability. It needs to feel premium and professional while still keeping a simple layout that fits a cybersecurity and IT brand.
Nice to have
• Nice to have elements include subtle touches that give the card a modern, tech feel, along with a layout that works well in different background styles.
Should not have
• The card should avoid clutter, loud graphics, or anything that takes attention away from the logo and contact details.

```html
<!DOCTYPE html>
<html lang="en">
<head>
<meta charset="utf-8">
<title>Quorvent Systems – Business Card</title>
<link href="https://fonts.googleapis.com/css2?family=Montserrat:wght@400;500;700&display=swap" rel="stylesheet">
<style>
  :root {
    --stage: #2b2b2d;
    --card: #050506;
    --white: #ffffff;
    --blue: #4f7fd8;
    --violet: #8a4fd6;
    --muted: #d9d9e0;
  }
  * { margin: 0; padding: 0; box-sizing: border-box; }
  html, body { width: 1200px; height: 875px; overflow: hidden; }
  body {
    background: var(--stage);
    font-family: "Montserrat", sans-serif;
    position: relative;
  }
  .card {
    position: absolute;
    width: 540px;
    height: 310px;
    background: var(--card);
    border-radius: 16px;
    box-shadow: 0 18px 40px rgba(0,0,0,.55);
    overflow: hidden;
  }
  .card--front { left: 50px; top: 140px; }
  .card--back { left: 610px; top: 425px; }

  /* front */
  .front-brand {
    position: absolute;
    inset: 0;
    display: flex;
    align-items: center;
    justify-content: center;
    gap: 16px;
  }
  .brand-mark {
    width: 44px; height: 44px;
    border: 4px solid var(--white);
    flex: none;
  }
  .brand-name {
    color: var(--white);
    font-weight: 700;
    font-size: 38px;
    letter-spacing: .5px;
    white-space: nowrap;
  }

  /* back */
  .back-brand {
    position: absolute;
    left: 30px;
    top: 50%;
    transform: translateY(-50%);
    display: flex;
    align-items: center;
    gap: 9px;
  }
  .back-brand .brand-mark { width: 20px; height: 20px; border: 3px solid var(--blue); }
  .back-brand .brand-name { font-size: 16px; letter-spacing: 0; color: var(--blue); }

  .divider {
    position: absolute;
    left: 272px;
    top: 70px;
    width: 2px;
    height: 170px;
    background: linear-gradient(var(--violet), var(--blue));
  }
  .contact {
    position: absolute;
    left: 292px;
    top: 70px;
    color: var(--white);
    white-space: nowrap;
  }
  .contact-name {
    font-weight: 700;
    font-size: 23px;
    background: linear-gradient(90deg, var(--blue), var(--violet));
    -webkit-background-clip: text;
    background-clip: text;
    color: transparent;
  }
  .contact-role { font-size: 10.5px; color: var(--muted); margin-top: 3px; }
  .contact-list { list-style: none; margin-top: 18px; }
  .contact-list li {
    display: flex;
    align-items: center;
    gap: 10px;
    font-size: 13px;
    margin-bottom: 10px;
  }
  .contact-list svg { width: 14px; height: 14px; fill: var(--violet); flex: none; }
</style>
</head>
<body>
  <section class="card card--front" aria-label="Card front">
    <div class="front-brand">
      <span class="brand-mark"></span>
      <span class="brand-name">Quorvent Systems</span>
    </div>
  </section>

  <section class="card card--back" aria-label="Card back">
    <div class="back-brand">
      <span class="brand-mark"></span>
      <span class="brand-name">Quorvent Systems</span>
    </div>
    <div class="divider"></div>
    <div class="contact">
      <h1 class="contact-name">Dana Holloway</h1>
      <p class="contact-role">Owner | CEO | Quorvent Systems</p>
      <ul class="contact-list">
        <li>
          <svg viewBox="0 0 16 16"><path d="M2 6c0-2 2-3 6-3s6 1 6 3v1h-3V5.5H5V7H2z M3 8h10l1 6H2z"/></svg>
          (800) 555-0142
        </li>
        <li>
          <svg viewBox="0 0 16 16"><path d="M3 1l3 3-1.5 2a9 9 0 0 0 5.5 5.5L12 10l3 3-2 2C6 15 1 10 1 3z"/></svg>
          (555) 555-0187
        </li>
        <li>
          <svg viewBox="0 0 16 16"><path d="M1 3h14v1L8 9 1 4z M1 6l7 5 7-5v7H1z"/></svg>
          dana@quorvent.com
        </li>
        <li>
          <svg viewBox="0 0 16 16"><circle cx="8" cy="8" r="7"/><path d="M1 8h14M8 1c3 3 3 11 0 14M8 1c-3 3-3 11 0 14" stroke="#050506" stroke-width="1.2" fill="none"/></svg>
          www.quorvent.com
        </li>
      </ul>
    </div>
  </section>
</body>
</html>
```